PowerPoint design MedoraVix

We need a PowerPoint set-up based upon our existing logo (see joint file)
Our company is operating in the health care and life science sector. We are mainly focussing on international business

Target Market(s)

International

Industry/Entity Type

health care and life sciences

Requirements
Must have
• Logos as added

```html
<!DOCTYPE html>
<html lang="en">
<head>
<meta charset="utf-8">
<title>MedoraVix – Table of Content</title>
<link rel="stylesheet" href="https://fonts.googleapis.com/css2?family=Carlito:wght@400;700&display=swap">
<style>
  :root {
    --navy: #0b4a80;
    --navy-line: #2b6698;
    --green: #6cc24a;
    --text: #444444;
    --paper: #ffffff;
  }
  * { margin: 0; padding: 0; box-sizing: border-box; }
  html, body { width: 1200px; height: 675px; overflow: hidden; background: var(--paper); }
  body { font-family: "Carlito", Calibri, Arial, sans-serif; color: var(--text); }
  .slide { position: relative; width: 1200px; height: 675px; background: var(--paper); }

  .helix-band {
    position: absolute; height: 22px;
    background: linear-gradient(90deg, var(--navy), var(--green));
    border-radius: 11px; opacity: .85;
  }
  .helix-band.left { left: 0; top: 65px; width: 62px; border-radius: 0 11px 11px 0; }
  .helix-band.right { right: 0; top: 70px; width: 58px; border-radius: 11px 0 0 11px; }

  .slide-title {
    position: absolute; left: 72px; top: 56px;
    font-size: 34px; font-weight: 700; color: var(--navy); letter-spacing: -0.2px;
  }

  .brand { position: absolute; left: 955px; top: 56px; display: flex; align-items: center; gap: 10px; }
  .brand-dot { width: 42px; height: 42px; border-radius: 50%; background: var(--navy); }
  .brand-name { font-size: 25px; font-weight: 700; color: var(--navy); }

  .toc-item { position: absolute; height: 40px; }
  .toc-item .num {
    position: absolute; left: 0; top: 0; width: 36px; height: 36px;
    border: 1.3px solid var(--navy-line); border-radius: 50%;
    display: flex; align-items: center; justify-content: center;
    font-size: 20px; font-weight: 700; color: var(--navy); background: var(--paper);
  }
  .toc-item .rule { position: absolute; left: 36px; top: 18px; height: 1.3px; background: var(--navy-line); }
  .toc-item .heading { position: absolute; left: 61px; top: -7px; font-size: 16.5px; font-weight: 700; color: var(--navy); white-space: nowrap; }
  .toc-item .sub { position: absolute; left: 61px; top: 20px; font-size: 13.5px; color: var(--text); white-space: nowrap; }
  .col-left { left: 71px; width: 514px; }
  .col-right { left: 617px; width: 512px; }
  .col-left .rule { width: 477px; }
  .col-right .rule { width: 475px; }

  .footer-line { position: absolute; top: 616px; height: 1px; }
  .footer-line.navy { left: 0; width: 708px; background: var(--navy-line); }
  .footer-line.green { left: 1143px; width: 57px; background: var(--green); }
  .footer-dot { position: absolute; top: 612px; width: 8px; height: 8px; border-radius: 50%; }
  .footer-dot.navy { left: 704px; background: var(--navy); }
  .footer-dot.green { left: 1139px; background: var(--green); }
  .footer-title { position: absolute; left: 725px; top: 610px; font-size: 10.5px; font-variant: small-caps; letter-spacing: .3px; color: var(--text); }
  .page-number { position: absolute; left: 1113px; top: 610px; font-size: 11px; color: var(--text); }

  .notes { position: absolute; left: 72px; top: 620px; font-size: 7.5px; line-height: 10.3px; color: var(--text); }
</style>
</head>
<body>
<main class="slide">
  <div class="helix-band left" role="img" aria-label="Helix ornament in blue and green"></div>
  <h1 class="slide-title">Sample Table of Content</h1>

  <div class="brand">
    <span class="brand-dot"></span>
    <span class="brand-name">MedoraVix</span>
  </div>
  <div class="helix-band right" role="img" aria-label="Helix ornament in blue and green"></div>

  <section class="toc">
    <div class="toc-item col-left" style="top:159px"><span class="rule"></span><span class="num">1</span><span class="heading">Sample Section 1</span><span class="sub">Sample Section 1 Text</span></div>
    <div class="toc-item col-left" style="top:253px"><span class="rule"></span><span class="num">2</span><span class="heading">Sample Section 2</span><span class="sub">Sample Section 2 Text</span></div>
    <div class="toc-item col-left" style="top:349px"><span class="rule"></span><span class="num">3</span><span class="heading">Sample Section 3</span><span class="sub">Sample Section 3 Text</span></div>
    <div class="toc-item col-left" style="top:443px"><span class="rule"></span><span class="num">4</span><span class="heading">Sample Section 4</span><span class="sub">Sample Section 4 Text</span></div>
    <div class="toc-item col-left" style="top:538px"><span class="rule"></span><span class="num">5</span><span class="heading">Sample Section 5</span><span class="sub">Sample Section 5 Text</span></div>

    <div class="toc-item col-right" style="top:159px"><span class="rule"></span><span class="num">6</span><span class="heading">Sample Section 1</span><span class="sub">Sample Section 1 Text</span></div>
    <div class="toc-item col-right" style="top:253px"><span class="rule"></span><span class="num">7</span><span class="heading">Sample Section 2</span><span class="sub">Sample Section 2 Text</span></div>
    <div class="toc-item col-right" style="top:349px"><span class="rule"></span><span class="num">8</span><span class="heading">Sample Section 3</span><span class="sub">Sample Section 3 Text</span></div>
    <div class="toc-item col-right" style="top:443px"><span class="rule"></span><span class="num">9</span><span class="heading">Sample Section 4</span><span class="sub">Sample Section 4 Text</span></div>
    <div class="toc-item col-right" style="top:538px"><span class="rule"></span><span class="num">10</span><span class="heading">Sample Section 5</span><span class="sub">Sample Section 5 Text</span></div>
  </section>

  <footer>
    <span class="footer-line navy"></span>
    <span class="footer-dot navy"></span>
    <span class="footer-title">Presentation Title</span>
    <span class="page-number">10</span>
    <span class="footer-dot green"></span>
    <span class="footer-line green"></span>
    <div class="notes">
      <p>Source: Sample source text</p>
      <p><sup>1</sup> Sample notes text 1</p>
      <p><sup>2</sup> Sample notes text 2</p>
    </div>
  </footer>
</main>
</body>
</html>
```